Super urgent - business card design

I need to design a business card
on the front side the words "VORTAL CAPITAL" with the top half surrounded by a stylised cloud. Minimalist, navy blue font on white background, with the Vortal capital in embossing.

On the back contact details (avoid centered). I would rather have the details taking the 2/3rd on the right and having the logo on the left, but anyway not plain centered

Renato Lo Cascio
CEO e Fondatore

r.locascio@vortal-capital.example
+39.347.512.6084

Piazza Torcelli 7
20135 Milano

```html
<!DOCTYPE html>
<html lang="it">
<head>
<meta charset="utf-8">
<title>Vortal Capital – Business Card</title>
<link rel="stylesheet" href="https://fonts.googleapis.com/css2?family=Cinzel:wght@500&family=Tinos:wght@400;700&display=swap">
<style>
  :root {
    --backdrop: #1c1c1c;
    --card-front: #ffffff;
    --card-back: #efefef;
    --navy: #14195a;
    --navy-deep: #1b2470;
  }
  * { margin: 0; padding: 0; box-sizing: border-box; }
  html, body {
    width: 1200px;
    height: 1059px;
    overflow: hidden;
    background: var(--backdrop);
  }
  .canvas {
    position: relative;
    width: 1200px;
    height: 1059px;
  }
  .card {
    position: absolute;
    border-radius: 24px;
    overflow: hidden;
  }
  .card--details {
    left: 257px;
    top: 89px;
    width: 691px;
    height: 394px;
    background: var(--card-front);
  }
  .card--brand {
    left: 259px;
    top: 546px;
    width: 701px;
    height: 399px;
    background: var(--card-back);
  }

  /* Details side */
  .brand-name {
    position: absolute;
    left: 46px;
    top: 186px;
    width: 240px;
    font-family: "Cinzel", serif;
    font-weight: 500;
    font-size: 38px;
    line-height: 42px;
    color: var(--navy);
    letter-spacing: 0.5px;
  }
  .divider {
    position: absolute;
    left: 303px;
    top: 63px;
    width: 1.5px;
    height: 263px;
    background: var(--navy);
  }
  .contact {
    position: absolute;
    left: 349px;
    top: 62px;
    font-family: "Tinos", serif;
    color: var(--navy);
  }
  .contact__name {
    font-weight: 700;
    font-size: 24px;
    line-height: 28px;
  }
  .contact__role {
    font-size: 16px;
    line-height: 20px;
    margin-top: 2px;
  }
  .contact__address {
    font-size: 20px;
    line-height: 25px;
    margin-top: 41px;
  }
  .contact__rule {
    width: 30px;
    height: 2px;
    background: var(--navy);
    margin: 14px 0 0 -2px;
  }
  .contact__lines {
    font-size: 19px;
    line-height: 29.5px;
    margin-top: 30px;
  }

  /* Brand side */
  .wordmark {
    position: absolute;
    left: 0;
    width: 100%;
    text-align: center;
    font-family: "Cinzel", serif;
    font-weight: 500;
    color: var(--navy-deep);
  }
  .wordmark--main {
    top: 128px;
    font-size: 60px;
    line-height: 70px;
    letter-spacing: 24px;
    text-indent: 24px;
  }
  .wordmark--sub {
    top: 232px;
    font-size: 24px;
    line-height: 30px;
    letter-spacing: 27px;
    text-indent: 27px;
  }
</style>
</head>
<body>
  <main class="canvas">
    <section class="card card--details" aria-label="Lato contatti">
      <div class="brand-name">VORTAL CAPITAL</div>
      <div class="divider"></div>
      <div class="contact">
        <p class="contact__name">Renato Lo Cascio</p>
        <p class="contact__role">CEO e Fondatore</p>
        <p class="contact__address">Piazza Torcelli 7<br>20135 Milano</p>
        <div class="contact__rule"></div>
        <p class="contact__lines">
          +39.347.512.6084<br>
          r.locascio@vortal-capital.example<br>
          www.vortal-capital.example
        </p>
      </div>
    </section>

    <section class="card card--brand" aria-label="Lato marchio">
      <p class="wordmark wordmark--main">VORTAL</p>
      <p class="wordmark wordmark--sub">CAPITAL</p>
    </section>
  </main>
</body>
</html>
```